High-end dermatology office brochure design

Corvella Skin and Laser is a high-end dermatology practice that specializes in custom skin care solutions, and skin cancer surveillance and treatment. Brochure should be elegant, but informative to attract high-end customers.

Target Market(s)

Men and women 27-60

Industry/Entity Type

Office

Requirements
Must have
• Attached document has required copy, including, websites, address and company phone number
Nice to have
• images

```html
<!DOCTYPE html>
<html lang="en">
<head>
<meta charset="utf-8">
<title>Corvella Skin and Laser Brochure</title>
<link href="https://fonts.googleapis.com/css2?family=Bebas+Neue&family=Oleo+Script&family=Ubuntu:wght@400;500&display=swap" rel="stylesheet">
<style>
:root{
  --purple:#6b2f86;
  --lime:#d3e27d;
  --lime-text:#cfe07a;
  --green-text:#9dbb45;
  --pale:#eef3d8;
  --ink:#2e2e2e;
  --stage:#6d6f72;
  --white:#ffffff;
}
*{margin:0;padding:0;box-sizing:border-box}
html,body{width:1179px;height:1200px;overflow:hidden;background:var(--stage)}
body{position:relative;font-family:'Ubuntu',sans-serif;color:var(--ink)}
.spread{position:absolute;left:66px;width:1051px;height:526px;overflow:hidden;background:var(--white)}
.spread--outside{top:61px}
.spread--inside{top:619px;background:var(--pale)}
.abs{position:absolute}
.contact{left:0;width:526px;top:30px;text-align:center;font-weight:500;font-size:17px;line-height:21.5px;color:var(--purple)}
.contact .shop{color:var(--green-text)}
.locations{left:0;top:114px;width:526px;height:310px;background:var(--purple);color:var(--white)}
.display{font-family:'Bebas Neue',sans-serif;letter-spacing:.5px}
.locations h2{position:absolute;top:26px;width:100%;text-align:center;font-weight:400;font-size:28px;color:var(--lime-text)}
.locations .rule{position:absolute;left:34px;top:65px;width:459px;height:1px;background:rgba(255,255,255,.55)}
.location{position:absolute;top:84px;width:160px;margin-left:-80px;text-align:center}
.location h3{font-weight:500;font-size:10.5px;height:30px}
.map{width:101px;height:101px;margin:0 auto;border-radius:50%;border:3px solid var(--lime);background:#e6e4de}
.location p{margin-top:18px;font-size:8.6px;line-height:13.5px}
.brand{font-weight:500;color:var(--purple);white-space:nowrap}
.brand::before{content:"";display:inline-block;width:9px;height:9px;border-radius:50%;background:var(--lime);margin-right:6px;vertical-align:1px}
.brand--back{left:0;width:526px;top:456px;text-align:center;font-size:18px}
.insurance{left:0;width:526px;top:506px;text-align:center;font-size:7px}
.photo-front{left:526px;top:0;width:525px;height:440px;background:linear-gradient(100deg,#e9c7b3 0%,#f1d9cb 45%,#f7ece6 62%,#ffffff 75%)}
.brand--cover{left:800px;top:188px;font-size:17px}
.front-bands{left:526px;top:0}
.about{left:801px;top:355px;width:232px;font-size:9px;line-height:13.5px}
.tagline{left:526px;width:525px;top:450px;font-family:'Oleo Script',cursive;color:var(--lime-text);font-size:23px;line-height:29px}
.tagline span{display:block}
.tag{position:absolute;background:var(--purple);color:var(--white);font-size:29px;line-height:34px;height:34px;padding:0 0 0 33px;white-space:nowrap}
.medical-tag{left:0;top:23px;width:225px}
.surgery-tag{left:0;top:368px;width:365px}
.cosmetic-tag{left:826px;top:23px;width:225px;padding-left:10px}
.nutrition-tag{left:526px;top:429px;width:397px;padding-left:33px}
.copy{font-size:10.8px;line-height:16px}
.copy h4{font-weight:400;color:var(--purple);font-size:10.8px}
.medical{left:35px;top:70px;width:480px}
.conditions{left:35px;top:95px;width:455px;display:flex;justify-content:space-between}
.conditions span{width:55px;height:55px;border-radius:50%;background:var(--lime);color:var(--purple);font-family:'Bebas Neue',sans-serif;font-size:12.5px;display:flex;align-items:center;justify-content:center}
.photo-inside{left:526px;top:0;width:300px;height:414px;background:linear-gradient(160deg,#f1ead9 0%,#c9957a 50%,#a3705a 100%)}
.nutrition-band{left:526px;top:414px;width:525px;height:112px;background:var(--lime)}
.nutrition{left:560px;top:478px;width:460px;font-size:10.5px;line-height:16px}
.cosmetic{left:836px;top:73px;width:198px;font-size:9.5px;line-height:14.7px}
.cosmetic h4{color:var(--ink);font-weight:500;font-size:9.5px}
.cosmetic ul{list-style:none}
.cosmetic li{padding-left:7px;text-indent:-7px}
</style>
</head>
<body>

<section class="spread spread--outside">
  <div class="abs contact">
    <div>Call 480-555-0182</div>
    <div>corvellaskincare.com</div>
    <div class="shop">Shop at 2cherishyourskin.com</div>
  </div>

  <div class="abs locations">
    <h2 class="display">Visit Our Locations</h2>
    <div class="rule"></div>
    <div class="location" style="left:110px">
      <h3>Phoenix, Arizona</h3>
      <div class="map" role="img" aria-label="Street map of the Phoenix office"></div>
      <p>Corvella Skin &amp; Laser<br>4780 E Sonora Rd<br>Building #9<br>Suite #148<br>Phoenix, AZ 85044</p>
    </div>
    <div class="location" style="left:263px">
      <h3>Scottsdale, Arizona</h3>
      <div class="map" role="img" aria-label="Street map of the Scottsdale office"></div>
      <p>Pure Dermis Solutions<br>Located in Wellness Commons<br>9320 E Canyon Vista<br>Suite #103<br>Scottsdale, AZ 85260</p>
    </div>
    <div class="location" style="left:416px">
      <h3>Island Skin Cancer Center</h3>
      <div class="map" role="img" aria-label="Street map of the Honolulu office"></div>
      <p>Two Harborview Plaza<br>Suite #470<br>720 Kaimana Blvd.<br>Honolulu, HI 96815</p>
    </div>
  </div>

  <div class="abs brand brand--back">Corvella Skin &amp; Laser</div>
  <div class="abs insurance">We accept most major insurances and offer affordable self-pay rates.</div>

  <div class="abs photo-front" role="img" aria-label="Close-up beauty portrait photograph of a woman with clear skin"></div>
  <div class="abs brand brand--cover">Corvella Skin &amp; Laser</div>

  <svg class="abs front-bands" width="525" height="526" viewBox="0 0 525 526">
    <polygon points="156,352 525,340 525,440 156,440" fill="var(--lime)"/>
    <polygon points="0,429 525,440 525,526 0,526" fill="var(--purple)"/>
  </svg>
  <p class="abs about">We pride ourselves on providing premium skin care, to patients of all ages, with an honest and attentive approach. We're also proud to be leaders in skin cancer surveillance and specialize in the diagnosis and treatment of skin cancer.</p>
  <div class="abs tagline">
    <span style="padding-left:30px">Let us create a custom skin care regimen</span>
    <span style="padding-left:53px">that best fits your medical and personal needs</span>
  </div>
</section>

<section class="spread spread--inside">
  <div class="tag medical-tag display">Medical Services</div>
  <div class="abs copy medical">We're leaders in the diagnosis of all skin conditions and autoimmune skin conditions, including:</div>
  <div class="abs conditions">
    <span>Rashes</span><span>Acne</span><span>Warts</span><span>Skin Tags</span><span>Rosacea</span><span>Psoriasis</span>
  </div>
  <div class="abs copy" style="left:35px;top:160px;width:440px">
    <p>We're also involved in ongoing research for the treatment of psoriasis.</p>
    <h4 style="margin-top:16px">Skin cancer surveillance and treatment</h4>
    <p>Skin cancer can form anywhere on the skin (even where the sun doesn't shine), so it's vital that a full body exam is done at least once a year.</p>
    <p style="margin-top:16px">We pride ourselves on thorough surveillance and commitment to your overall health.</p>
    <h4 style="margin-top:16px">Alternative care</h4>
    <p>Your commitment to your health is the same as our commitment to you.<br>We provide non-antibiotic acne treatment including botanicals, blue light and a combination of supplements to fit your personal lifestyle.</p>
  </div>

  <div class="tag surgery-tag display">Dermatologic Surgery Services</div>
  <div class="abs copy" style="left:35px;top:410px;width:480px">
    <p>We have in-house surgeons for the removal of atypical moles and skin cancers,<br>including margin control for melanoma.</p>
    <p style="margin-top:16px">Our board-certified, in-house surgeons specialize in:<br>- Plastic surgery<br>- Mohs surgery (treatment includes transportation and care from your trusted healthcare team)</p>
  </div>

  <div class="abs photo-inside" role="img" aria-label="Portrait photograph of a woman looking upward"></div>

  <div class="tag cosmetic-tag display">Cosmetic Services</div>
  <div class="abs cosmetic">
    <p>Your skin is unique, so we take pride in our ability to provide personalized consultations and skin care analysis to set you up with the right treatments and products.</p>
    <ul style="margin-top:14px">
      <li>- Chemical peels</li>
      <li>- Photofacial</li>
      <li>- Sonalift</li>
      <li>- Lumiva</li>
      <li>- IPL</li>
      <li>- Injectables and fillers (Fillara, Plumvessa, Qorvelline, Neurotox and Smoothera)</li>
    </ul>
    <h4 style="margin-top:14px">Elite-grade cosmeceutical products</h4>
    <p>Including Verelle, Jana Moreau, Lumage, Tintology, Dermascript, Lashora and much more.</p>
    <h4 style="margin-top:14px">Eesthetic services</h4>
    <p>Facials, peels, microdermabrasion, body wraps, waxing, eyelash extensions, brow tinting</p>
  </div>

  <div class="abs nutrition-band"></div>
  <div class="tag nutrition-tag display">Nutrition and Supplement Support</div>
  <p class="abs nutrition">Including gluten free, no filler multi-vitamins, immune boosters, hormone, sleep aid balancing products and B12 injections and the Slim Shot.</p>
</section>

</body>
</html>
```